Political Candidate Newspaper Advertisement

I would like a newspaper ad for my campaign for election to City Council. The banner ad is 10 cm high x 26.2 cm wide. The banner will contain a photo and the following text (or words to similar effect):
VOTE
COLIN DRAY
COMO BEACH
For a
SAFE
CARING
CONNECTED
COMMUNITY
Lifetime commitment to local clubs, charities and international aid
Local business owner
Founder of Open-Gate Fete
Councillor, Mediator, B.Sc., MBA
The Councillor you know and can call for help
Respects our heritage and our future
Listens to the wisdom and needs of older residents
Promotes more young people
Protects our South Perth environment
Authorised by Colin Dray 4/87 Tilbury St, Como. 9381 7264
I use MS Publisher and PhotoShop so I'd like the product to be in a form I can use. After ther banner ad is done, and if it is good, I wish to pay the designer to use the same theme to produce another newspaper ad, a brochure and a poster.
My simple version is attached. A photo is also attached.
I'm hoping you do better.
Target Market(s)
18-80 years old
Industry/Entity Type
Business
Requirements
Must have
- simple fonts
Nice to have
- A TICK somewhere around the word Vote would be good.
Mention of www.harlowvoice.net if possible, perhaps at the bottom of the page, along with the Authorised by ... text.

```html
<!DOCTYPE html>
<html lang="en">
<head>
<meta charset="utf-8">
<title>Vote Colin Dray – Como Beach</title>
<link href="https://fonts.googleapis.com/css2?family=Arimo:wght@700&family=Open+Sans:ital,wght@0,600;0,700;1,400&display=swap" rel="stylesheet">
<style>
  :root {
    --page: #ffffff;
    --frame: #3fe23a;
    --frame-dark: #1f9e1c;
    --red: #e10000;
    --purple: #7a1e9c;
    --blue: #0b2fd6;
    --white: #ffffff;
    --yellow: #fff200;
    --ink: #111111;
    --suit: rgba(30, 28, 60, .85);
    --skin: rgba(225, 170, 150, .9);
    --shirt: rgba(220, 200, 225, .85);
  }
  * { margin: 0; padding: 0; box-sizing: border-box; }
  html, body {
    width: 1200px; height: 601px; overflow: hidden;
    background: var(--page);
  }
  .canvas { position: relative; width: 1200px; height: 601px; }
  .banner {
    position: absolute; left: 75px; top: 98px; width: 1031px; height: 394px;
    border: 8px solid var(--frame);
    box-shadow: 2px 3px 4px rgba(0,0,0,.45), inset 0 0 0 1px var(--frame-dark);
    background: linear-gradient(180deg, var(--red) 0%, var(--red) 12%, var(--purple) 50%, var(--blue) 85%, var(--blue) 100%);
    overflow: hidden;
    font-family: "Open Sans", Arial, sans-serif;
    color: var(--white);
  }
  .portrait {
    position: absolute; left: 770px; top: 0; width: 245px; height: 378px; z-index: 0;
    background:
      radial-gradient(ellipse 50px 70px at 125px 80px, var(--skin) 0%, var(--skin) 70%, rgba(225,170,150,0) 100%),
      radial-gradient(ellipse 50px 120px at 145px 270px, var(--shirt) 0%, var(--shirt) 60%, rgba(220,200,225,0) 100%),
      radial-gradient(ellipse 150px 160px at 150px 320px, var(--suit) 0%, var(--suit) 65%, rgba(30,28,60,0) 100%);
  }
  .rule-row {
    position: absolute; left: 17px; width: 446px; z-index: 1;
    display: flex; align-items: center; justify-content: center; gap: 10px;
  }
  .rule-row::before, .rule-row::after {
    content: ""; flex: 1; height: 4px; background: var(--white);
    box-shadow: 1px 2px 2px rgba(0,0,0,.6);
  }
  .vote {
    top: 30px;
    font-family: "Arimo", Arial, sans-serif; font-weight: 700; font-size: 44px;
    color: var(--yellow); line-height: 1;
    -webkit-text-stroke: 2px var(--ink); paint-order: stroke fill;
    text-shadow: 2px 2px 2px rgba(0,0,0,.7);
  }
  .candidate {
    position: absolute; left: 15px; top: 74px; width: 452px; z-index: 1;
    font-family: "Arimo", Arial, sans-serif; font-weight: 700; font-size: 76px;
    letter-spacing: -1px; line-height: 1; text-align: center;
    text-shadow: 2px 3px 2px rgba(0,0,0,.75);
  }
  .ward {
    top: 154px; width: 400px;
    font-family: "Open Sans", Arial, sans-serif; font-weight: 600; font-size: 38px;
    color: var(--yellow); line-height: 1;
    text-shadow: 2px 2px 2px rgba(0,0,0,.7);
  }
  .ward::before { flex: 0 0 62px; }
  .ward::after { flex: 0 0 18px; }
  .for-a {
    top: 212px;
    font-family: "Arimo", Arial, sans-serif; font-weight: 700; font-size: 37px; line-height: 1;
    text-shadow: 2px 2px 2px rgba(0,0,0,.7);
  }
  .slogan {
    position: absolute; left: 15px; top: 250px; width: 452px; text-align: center; z-index: 1;
    font-family: "Arimo", Arial, sans-serif; font-weight: 700; line-height: 1;
    text-shadow: 2px 3px 2px rgba(0,0,0,.7);
  }
  .slogan .big { display: block; font-size: 57px; letter-spacing: 0.5px; }
  .slogan .small { display: block; font-size: 32px; margin-top: 6px; letter-spacing: 0.3px; }
  .big-tick {
    position: absolute; left: 412px; top: 88px; width: 122px; height: 126px; z-index: 1;
  }
  .pledges {
    position: absolute; left: 531px; top: 19px; width: 330px; list-style: none; z-index: 2;
  }
  .pledges li {
    position: absolute; left: 0; display: flex; align-items: flex-start; gap: 8px;
    font-weight: 700; font-size: 13.5px; line-height: 15px;
    text-shadow: 1px 1px 2px rgba(0,0,0,.7); white-space: nowrap;
  }
  .pledges li svg { flex: 0 0 25px; width: 25px; height: 25px; margin-top: -3px; }
  .pledges small { font-size: 11px; }
  .authorised {
    position: absolute; left: 563px; top: 357px; z-index: 2;
    font-style: italic; font-weight: 400; font-size: 10px; color: var(--yellow);
  }
</style>
</head>
<body>
<svg width="0" height="0" style="position:absolute" aria-hidden="true">
  <symbol id="tick-badge" viewBox="0 0 25 25">
    <circle cx="11" cy="14" r="10" fill="#ffffff" stroke="#bbbbbb" stroke-width="1"/>
    <path d="M5 13 L10 19 L23 2 L10 14 Z" fill="#22c81f" stroke="#0f7a0d" stroke-width="0.8"/>
  </symbol>
</svg>
<div class="canvas">
  <section class="banner">
    <div class="portrait" role="img" aria-label="Portrait photo of the candidate in a dark suit, striped shirt and green patterned tie"></div>
    <div class="rule-row vote">VOTE</div>
    <h1 class="candidate">Colin Dray</h1>
    <div class="rule-row ward">COMO BEACH</div>
    <svg class="big-tick" viewBox="0 0 122 126" aria-hidden="true">
      <path d="M4 70 Q20 58 30 66 L48 96 Q80 36 118 4 Q116 12 108 20 Q70 66 52 122 Q44 126 36 118 Q22 92 4 70 Z" fill="#33e02d" stroke="#0c6f0a" stroke-width="2.5"/>
      <path d="M14 70 Q24 66 30 72 L46 100" fill="none" stroke="#b8ffb0" stroke-width="3" stroke-linecap="round"/>
    </svg>
    <div class="rule-row for-a">FOR A</div>
    <p class="slogan"><span class="big">SAFE, CARING</span><span class="small">CONNECTED COMMUNITY</span></p>
    <ul class="pledges">
      <li style="top:0"><svg><use href="#tick-badge"/></svg><span>Lifetime commitment to local clubs,<br>charities and international aid</span></li>
      <li style="top:46px"><svg><use href="#tick-badge"/></svg><span>Local business owner</span></li>
      <li style="top:76px"><svg><use href="#tick-badge"/></svg><span>Founder of Open-Gate Fete</span></li>
      <li style="top:107px"><svg><use href="#tick-badge"/></svg><span>Councillor, Mediator, <small>B.Sc., MBA</small></span></li>
      <li style="top:138px"><svg><use href="#tick-badge"/></svg><span>The Councillor you know and<br>can call for help</span></li>
      <li style="top:184px"><svg><use href="#tick-badge"/></svg><span>Respects our heritage and<br>our future</span></li>
      <li style="top:230px"><svg><use href="#tick-badge"/></svg><span>Listens to the wisdom and needs<br>of older residents</span></li>
      <li style="top:275px"><svg><use href="#tick-badge"/></svg><span>Promotes more young people</span></li>
      <li style="top:305px"><svg><use href="#tick-badge"/></svg><span>Protects our South Perth environment</span></li>
    </ul>
    <p class="authorised">Authorised by Colin Dray 4/87 Tilbury St, Como. 9381 7264</p>
  </section>
</div>
</body>
</html>
```